Commercial Piping Company Needs A Modern Business Card

We need a clean business card for our commercial pipe lining company. We would like to see a mock up in two color schemes: Black, Grey and Blue and Black, Grey and Orange. We are in the piping industry, but want a professional, clean and modern look to the card.

Industry/Entity Type

Plumbing

Contact Information for Business Card

Name: Mark Tollen
Title: Managing Partner
Phone: 382.615.9073
Email: Mark@VantoPipe.Net

Requirements
Must have
• Back Side Should Have a White Back Ground with Full Logo. Front I would like to see a couple lay outs for contact info. Also the final card will have rounded edges, so please take that into account for printing.
Nice to have
• Two Color Palette Examples
Should not have
• No need for an address line

```html
<!DOCTYPE html>
<html lang="en">
<head>
<meta charset="utf-8">
<title>VantoPipe Business Card</title>
<link href="https://fonts.googleapis.com/css2?family=Montserrat:wght@300;400;600;700&family=Open+Sans:wght@400&family=Roboto+Condensed:wght@700&display=swap" rel="stylesheet">
<style>
  :root {
    --bg: #2a2a2c;
    --card-white: #f4f4f4;
    --ink: #1e1e1e;
    --muted: #5a5a5e;
    --white: #f5f5f5;
    --soft: #b9b9bd;
    --blue: #4cc3d6;
  }
  * { box-sizing: border-box; margin: 0; padding: 0; }
  html, body { width: 1200px; height: 900px; overflow: hidden; background: var(--bg); }
  .canvas { position: relative; width: 1200px; height: 900px; }

  .card {
    position: absolute; left: 300px; width: 600px; height: 343px;
    border-radius: 26px; overflow: hidden;
  }
  .card--back { top: 60px; background: var(--card-white); }
  .card--front { top: 470px; background: linear-gradient(135deg, #1e1e1f 0%, #141415 100%); }

  .brand { position: absolute; font-family: "Montserrat", sans-serif; }
  .brand__name { font-weight: 600; line-height: 1; letter-spacing: 0.5px; }
  .brand__tag { letter-spacing: 1.2px; line-height: 1.5; white-space: nowrap; }
  .brand__tag--accent { color: var(--blue); }

  .card--back .brand { left: 0; right: 0; top: 128px; text-align: center; }
  .card--back .brand__name { font-size: 44px; color: var(--ink); margin-bottom: 8px; }
  .card--back .brand__tag { font-size: 13px; color: var(--muted); }
  .card--back .brand__tag--accent { color: var(--blue); }

  .card--front .brand { left: 352px; top: 68px; }
  .card--front .brand__name { font-size: 24px; color: var(--white); margin-bottom: 4px; }
  .card--front .brand__tag { font-size: 8px; color: var(--soft); }
  .card--front .brand__tag--accent { color: var(--blue); }

  .rule { position: absolute; height: 1px; background: var(--blue); }
  .rule--top { left: 40px; top: 92px; width: 296px; }
  .rule--name { left: 40px; top: 196px; width: 150px; }

  .person { position: absolute; left: 40px; top: 128px; font-family: "Montserrat", sans-serif; color: var(--white); }
  .person__name { font-size: 30px; letter-spacing: 0.5px; line-height: 1; }
  .person__first { font-weight: 300; }
  .person__last { font-weight: 700; }
  .person__title { font-family: "Roboto Condensed", sans-serif; font-weight: 700; font-size: 13px; color: var(--blue); margin-top: 6px; letter-spacing: 0.3px; }

  .contacts { position: absolute; left: 40px; top: 212px; list-style: none; font-family: "Open Sans", sans-serif; font-size: 15px; color: var(--white); }
  .contacts li { display: flex; align-items: center; gap: 12px; height: 28px; }
  .contacts svg { width: 15px; height: 15px; flex: none; }
</style>
</head>
<body>
<div class="canvas">

  <section class="card card--back" aria-label="Card back">
    <div class="brand">
      <div class="brand__name">VantoPipe</div>
      <div class="brand__tag brand__tag--accent">COMMERCIAL PIPE LINING</div>
      <div class="brand__tag">INSPECT • REPAIR • RENEW</div>
    </div>
  </section>

  <section class="card card--front" aria-label="Card front">
    <div class="rule rule--top"></div>
    <div class="brand">
      <div class="brand__name">VantoPipe</div>
      <div class="brand__tag brand__tag--accent">COMMERCIAL PIPE LINING</div>
      <div class="brand__tag">INSPECT • REPAIR • RENEW</div>
    </div>

    <div class="person">
      <div class="person__name"><span class="person__first">MARK</span> <span class="person__last">TOLLEN</span></div>
      <div class="person__title">MANAGING PARTNER</div>
    </div>
    <div class="rule rule--name"></div>

    <ul class="contacts">
      <li>
        <svg viewBox="0 0 16 16" aria-hidden="true"><path fill="#4cc3d6" d="M2 5c0-2 2-3 6-3s6 1 6 3v1h-3V5H5v1H2zM4 7h8l2 6H2z"/></svg>
        <span>382.615.9073</span>
      </li>
      <li>
        <svg viewBox="0 0 16 16" aria-hidden="true"><rect x="1" y="3" width="14" height="10" fill="#4cc3d6"/><path d="M1 3l7 6 7-6" stroke="#1b1b1c" stroke-width="1.4" fill="none"/></svg>
        <span>Mark@VantoPipe.Net</span>
      </li>
      <li>
        <svg viewBox="0 0 16 16" aria-hidden="true" fill="none" stroke="#4cc3d6" stroke-width="1.2"><circle cx="8" cy="8" r="6.5"/><ellipse cx="8" cy="8" rx="3" ry="6.5"/><path d="M1.5 8h13M2.5 5h11M2.5 11h11"/></svg>
        <span>VantoPipe.Net</span>
      </li>
    </ul>
  </section>

</div>
</body>
</html>
```